Geschäftspapiere für Unternehmensberatung
Zielgruppe
Wir machen Unternehmensberatung, Prozessoptimierung, Change Management,
Buchhaltung.
Unsere Zielgruppe sind Firmen, denen es wirtschaftlich nicht so gut geht und die Hilfe benötigen.
Aufgabenstellung
Wir möchten ein CI an unser Logo angepasst.
Es darf gerne etwas besonderes sein.

```html
<!DOCTYPE html>
<html lang="de">
<head>
<meta charset="utf-8">
<title>Kelta Consulting – Geschäftspapiere</title>
<link href="https://fonts.googleapis.com/css2?family=Cinzel:wght@600&family=Open+Sans:wght@400;600;700&display=swap" rel="stylesheet">
<style>
:root{
  --bg:#e9e9eb;
  --paper:#ffffff;
  --dark:#2a2a2c;
  --dark-flap:#252527;
  --blue:#1d4f9e;
  --green:#9bbf2b;
  --ink:#1d1d1f;
  --muted:#555558;
  --grey:#8a8a8d;
  --rule:#aaaaad;
  --light-text:#d9d9dc;
  --white:#ffffff;
}
*{margin:0;padding:0;box-sizing:border-box}
html,body{width:1200px;height:763px;overflow:hidden;background:var(--bg)}
body{font-family:"Open Sans",Arial,sans-serif;color:var(--ink);position:relative}
.piece{position:absolute}
.logo{font-family:"Cinzel",Georgia,serif;font-weight:600;color:var(--grey);display:flex;align-items:center;gap:5px;white-space:nowrap;letter-spacing:.02em}
.logo .dot{width:.9em;height:.9em;border-radius:50%;background:var(--blue);display:inline-block}
.logo.on-dark{color:var(--light-text)}
.card{width:152px;height:89px;background:var(--paper);padding:8px;font-size:4.5px;line-height:1.45}
.card.dark{background:var(--dark)}
.card .name{font-weight:700;font-size:6px;color:var(--ink)}
.card .name .accent{color:var(--blue)}
.card .role{font-size:4.5px;color:var(--muted)}
.card-1 .bottom-bar{position:absolute;left:0;right:0;bottom:0;height:4px;background:var(--blue)}
.card-1 .url{position:absolute;right:8px;bottom:4px;color:var(--white);font-size:4px;font-weight:600}
.card-2{border-left:3px solid var(--green)}
.contact-row{display:flex;align-items:center;gap:3px}
.contact-row i{width:3px;height:3px;border-radius:50%;background:var(--blue);display:inline-block}
.letter{left:399px;top:100px;width:288px;height:406px;background:var(--paper);padding:38px 26px 0}
.letter .date{text-align:right;font-size:6.5px;font-weight:600;margin-top:48px}
.letter .body{font-size:6.6px;line-height:1.32;text-align:justify;margin-top:16px;padding-left:16px}
.letter .body strong{font-size:7px}
.letter .body p+p{margin-top:10px}
.letter .sign{text-align:center;font-size:6.5px;margin-top:26px;padding-left:16px}
.letter .sign b{display:block;font-size:7px}
.letter .footer{position:absolute;left:30px;right:42px;bottom:22px;border-top:2px solid var(--rule);padding-top:6px;display:flex;justify-content:space-between;font-size:5.2px;font-weight:600;line-height:1.35}
.letter .footer div{display:flex;gap:4px;align-items:flex-start}
.letter .footer svg{flex:none}
.envelope{left:367px;top:530px;width:318px;height:158px;background:var(--dark)}
.envelope .flap{position:absolute;inset:0}
.envelope .logo{position:absolute;left:108px;top:48px;font-size:10px}
.reply-card{left:738px;top:68px;width:318px;height:163px;background:var(--dark)}
.reply-card .info{position:absolute;right:22px;top:130px;color:var(--white);font-size:5px;font-weight:600;text-align:right;line-height:1.35}
.reply-card .tab{position:absolute;right:14px;top:129px;width:5px;height:16px;background:var(--blue)}
.folder{left:737px;top:245px;width:320px;height:424px;background:var(--dark)}
.folder .logo{position:absolute;left:72px;top:186px;font-size:19px}
.folder .url{position:absolute;right:26px;bottom:38px;color:var(--white);font-size:7px;font-weight:700;display:flex;gap:5px;align-items:center}
.folder .url span{width:6px;height:6px;background:var(--blue)}
</style>
</head>
<body>

<!-- Business card: lawyer variant -->
<section class="piece card card-1" style="left:36px;top:69px">
  <div class="logo" style="position:absolute;right:8px;top:10px;font-size:7px"><span class="dot"></span>KELTA CONSULTING</div>
  <div style="position:absolute;left:8px;top:30px">
    <div class="name">INES VARLO</div>
    <div class="role">Geschäftsführer</div>
  </div>
  <div style="position:absolute;right:8px;top:42px;text-align:right">Lindenweg 14<br>80331 Musterstadt<br>Kanzlei Varlo GmbH</div>
  <div style="position:absolute;left:8px;top:60px">
    <div class="contact-row"><i></i>0711 000 12 34</div>
    <div class="contact-row"><i></i>info@kelta-beratung.de</div>
    <div class="contact-row"><i></i>Postfach 12, 80331</div>
  </div>
  <div style="position:absolute;right:8px;top:62px;font-weight:700;font-size:4.8px">Rechtsanwalt, LL.M., MBA</div>
  <div class="bottom-bar"></div>
  <div class="url">www.skizzenhafen.de</div>
</section>

<!-- Business card: director -->
<section class="piece card card-2" style="left:202px;top:69px">
  <div class="logo" style="position:absolute;left:4px;top:80px;transform:rotate(-90deg);transform-origin:left top;font-size:7px"><span class="dot"></span>KELTA CONSULTING</div>
  <div style="position:absolute;left:40px;top:12px;border-left:1px solid #999;padding-left:4px">
    <div class="name"><span class="accent">MILO</span> TESSARD</div>
    <div class="role">Director</div>
    <div style="margin-top:4px">
      <div class="contact-row"><i></i>(555) 010-4412</div>
      <div class="contact-row"><i></i>(555) 010-4413</div>
      <div class="contact-row"><i></i>milo@keltamail.com</div>
      <div class="contact-row"><i></i>48 Harbor Lane, Eastbrook, ST</div>
    </div>
  </div>
</section>

<!-- Business card: owner -->
<section class="piece card" style="left:36px;top:170px">
  <div class="logo" style="position:absolute;left:18px;top:22px;font-size:10px"><span class="dot"></span>KELTA CONSULTING</div>
  <div style="position:absolute;left:10px;top:52px;text-align:center">
    <div class="name" style="color:var(--blue)">Oren Valcourt</div>
    <div class="role">Owner-Director</div>
  </div>
  <div style="position:absolute;left:72px;top:50px;border-left:3px solid var(--blue);padding-left:4px">
    <div>07900 000 241</div>
    <div>oren@keltamail.com</div>
    <div>www.keltamail.com</div>
  </div>
</section>

<!-- Business card: dark back -->
<section class="piece card dark" style="left:202px;top:175px">
  <div class="logo on-dark" style="position:absolute;left:30px;top:38px;font-size:9px"><span class="dot"></span>KELTA CONSULTING</div>
</section>

<!-- Business card: staff -->
<section class="piece card" style="left:39px;top:271px;width:149px;height:86px">
  <div class="logo" style="position:absolute;right:8px;top:12px;font-size:8px"><span class="dot"></span>KELTA CONSULTING</div>
  <div style="position:absolute;left:8px;top:44px">
    <div class="name" style="color:var(--blue)">PAUL DERWIN</div>
    <div class="role">Director</div>
  </div>
  <div style="position:absolute;left:8px;top:66px">
    <div class="contact-row"><i></i>555-010-3675</div>
    <div class="contact-row"><i></i>paul@keltamail.com</div>
  </div>
  <div style="position:absolute;right:8px;top:66px;text-align:right">58 Alder Road<br>Lindholm, 04417</div>
</section>

<!-- Letterhead -->
<section class="piece letter">
  <div class="logo" style="font-size:11px"><span class="dot"></span>KELTA CONSULTING</div>
  <div class="date">Sep 27, 2019</div>
  <div class="body">
    <p><strong>Sep 27, 2019 (Brightline Market)</strong><br>
    Intelligence via NEWSWIRE -- A new market study on Global Pet Medicine Market with 100+ market data Tables, Pie Chart &amp; Graphs is released that will provide complete assessment of the Market and covers evolving trends, current scenario analysis and growth factors, and industry validated market data. The research study provides market breakdown by re</p>
    <p>venue and volume (if applicable) and price history estimates for Global Pet Medicine. Some are the key players from the coverage that are also part of the study are Arvenna, Tolmek, Caspia, Orlin, Veyra, Dunmore, Solvane, Mireau,</p>
  </div>
  <div class="sign"><b>SIGNATURE</b>Lena Ortvald</div>
  <div class="footer">
    <div><svg width="7" height="7" viewBox="0 0 10 10"><rect width="10" height="10" rx="1.5" fill="#1d1d1f"/><path d="M3 2.5l1.2 1.3-.6.8a5 5 0 0 0 1.8 1.8l.8-.6L7.5 7l-.8.8C4.8 7.6 2.4 5.2 2.2 3.3z" fill="#fff"/></svg><span>0532 000 118<br>0515 000 274</span></div>
    <div><svg width="7" height="7" viewBox="0 0 10 10"><rect width="10" height="10" rx="1.5" fill="#1d1d1f"/><path d="M2 3h6v4H2z M2 3l3 2.2L8 3" fill="none" stroke="#fff" stroke-width=".8"/></svg><span>info@keltamail.com<br>www.keltamail.com</span></div>
    <div><svg width="7" height="7" viewBox="0 0 10 10"><rect width="10" height="10" rx="1.5" fill="#1d1d1f"/><path d="M5 8.3S2.6 5.8 2.6 4.2a2.4 2.4 0 0 1 4.8 0C7.4 5.8 5 8.3 5 8.3z" fill="#fff"/></svg><span>412 - 8 Birch Rd | K4P210<br>Northvale</span></div>
  </div>
</section>

<!-- Envelope -->
<section class="piece envelope">
  <svg class="flap" width="318" height="158" viewBox="0 0 318 158" aria-hidden="true">
    <path d="M0 0H318V22Q318 30 300 38L178 80Q159 87 140 80L18 38Q0 30 0 22Z" fill="var(--dark-flap)"/>
  </svg>
  <div class="logo on-dark"><span class="dot"></span>KELTA CONSULTING</div>
</section>

<!-- Compliment card -->
<section class="piece reply-card">
  <div class="info">(555) 010-4412<br>office@keltamail.com<br>48 Harbor Lane, Eastbrook, ST 061</div>
  <div class="tab"></div>
</section>

<!-- Presentation folder -->
<section class="piece folder">
  <div class="logo on-dark"><span class="dot"></span>KELTA CONSULTING</div>
  <div class="url">www.kelta-beratung.com<span></span></div>
</section>

</body>
</html>
```